We are a all around maintence company for outdoor services. Commercial and residential: mowing, sprinkler repairs, power washing, parking lot striping, tree trimming, gutters cleaning, pond cleaning,feeding and fertilizing, flower bed clean up and fence repair.

Industry/Entity Type

It Company

Contact Information for Business Card

Bramblewick Yard Services
R.K. Mondavel
Cell 555-318-6047
P.O. Box 4518
Fernhollow,Zn 00000
Office 555-294-7730
Fax 555-294-7738

```html
<!DOCTYPE html>
<html lang="en">
<head>
<meta charset="utf-8">
<title>Bramblewick Yard Services – Business Card</title>
<link href="https://fonts.googleapis.com/css2?family=Playfair+Display:wght@700&family=Lato:wght@300;400;700&display=swap" rel="stylesheet">
<style>
  :root {
    --leaf: #8cb81f;
    --leaf-soft: #dfe9c4;
    --paper: #f1f1f1;
    --ink-grey: #8f8f8f;
    --edge-grey: #a3a3a3;
    --white: #ffffff;
    --backdrop: #e6e8e4;
  }
  * { box-sizing: border-box; margin: 0; padding: 0; }
  html, body { width: 1200px; height: 800px; overflow: hidden; }
  body {
    background: var(--backdrop);
    display: flex;
    align-items: center;
    justify-content: center;
    gap: 40px;
    font-family: "Lato", sans-serif;
  }
  .card {
    position: relative;
    width: 540px;
    height: 309px;
    background: var(--paper);
    box-shadow: 0 8px 24px rgba(0,0,0,0.15);
    overflow: hidden;
  }
  .wreath {
    position: absolute;
    border-radius: 50%;
    background: radial-gradient(ellipse at center, transparent 58%, var(--leaf-soft) 60%, transparent 72%);
  }
  .wordmark {
    position: relative;
    font-family: "Playfair Display", serif;
    font-weight: 700;
    color: var(--ink-grey);
    text-align: center;
    line-height: 1.1;
  }

  /* Front */
  .card-front .mark-area {
    position: absolute;
    top: 0; left: 0; right: 0;
    height: 265px;
    display: flex;
    align-items: center;
    justify-content: center;
  }
  .card-front .wreath { width: 250px; height: 230px; left: 145px; top: 18px; }
  .card-front .wordmark { font-size: 40px; }
  .card-front .band {
    position: absolute;
    left: 0; right: 0; bottom: 0;
    height: 44px;
    background: var(--leaf);
  }

  /* Back */
  .card-back { display: flex; }
  .card-back .edge {
    position: absolute;
    left: 0; top: 0;
    width: 20px; height: 309px;
  }
  .card-back .brand-panel {
    position: relative;
    width: 44%;
    display: flex;
    align-items: center;
    justify-content: center;
    padding-left: 20px;
  }
  .card-back .wreath { width: 130px; height: 120px; left: 54px; top: 94px; }
  .card-back .brand-panel .wordmark { font-size: 20px; }
  .card-back .contact-panel {
    width: 56%;
    background: var(--leaf);
    color: var(--white);
    padding: 64px 30px 0 34px;
  }
  .holder-name {
    font-size: 20px;
    letter-spacing: 0.5px;
    padding-bottom: 6px;
    border-bottom: 1px solid rgba(255,255,255,0.8);
    width: 150px;
    white-space: nowrap;
  }
  .holder-name .initials { font-weight: 300; }
  .holder-name .surname { font-weight: 700; }
  .contact-row {
    display: flex;
    align-items: center;
    gap: 14px;
    margin-top: 20px;
    font-size: 13px;
    line-height: 1.3;
  }
  .contact-row + .contact-row { margin-top: 12px; }
  .contact-icon { width: 30px; height: 36px; flex: none; }
</style>
</head>
<body>

  <section class="card card-front" aria-label="Business card front">
    <div class="mark-area">
      <div class="wreath" role="img" aria-label="Leafy vine wreath ornament"></div>
      <div class="wordmark">Bramblewick<br>Yard Services</div>
    </div>
    <div class="band"></div>
  </section>

  <section class="card card-back" aria-label="Business card back">
    <svg class="edge" viewBox="0 0 20 309" preserveAspectRatio="none" aria-hidden="true">
      <rect width="20" height="309" fill="var(--leaf)"/>
      <path d="M0 0 H20 V110 C20 122 12 128 0 134 Z" fill="var(--edge-grey)"/>
    </svg>

    <div class="brand-panel">
      <div class="wreath" role="img" aria-label="Leafy vine wreath ornament"></div>
      <div class="wordmark">Bramblewick<br>Yard Services</div>
    </div>

    <div class="contact-panel">
      <div class="holder-name"><span class="initials">R.K.</span> <span class="surname">MONDAVEL</span></div>

      <div class="contact-row">
        <svg class="contact-icon" viewBox="0 0 30 36" aria-hidden="true">
          <path d="M3 2 H27 V26 L15 34 L3 26 Z" fill="var(--white)"/>
          <path d="M8 14 C8 9 22 9 22 14 L19 15 L18 13 H12 L11 15 Z" fill="var(--leaf)"/>
          <rect x="9" y="16" width="12" height="7" rx="1.5" fill="var(--leaf)"/>
          <circle cx="15" cy="19.5" r="2" fill="var(--white)"/>
        </svg>
        <div>
          Cell 555-318-6047<br>
          Office 555-294-7730<br>
          Fax 555-294-7738
        </div>
      </div>

      <div class="contact-row">
        <svg class="contact-icon" viewBox="0 0 30 36" aria-hidden="true">
          <path d="M3 2 H27 V26 L15 34 L3 26 Z" fill="var(--white)"/>
          <path d="M15 8 L23 15 H20.5 V23 H9.5 V15 H7 Z" fill="var(--leaf)"/>
          <rect x="13.5" y="18" width="3" height="5" fill="var(--white)"/>
        </svg>
        <div>
          P.O. Box 4518<br>
          Fernhollow,Zn 00000
        </div>
      </div>
    </div>
  </section>

</body>
</html>
```